1 Home page redesign for existing repair service site.

We need a refresh of our existing website that looks more 2017. We have made a mockup of the content that we want and a sample of where we want it. Nothing is set in stone, if you have better ideas of where things should go, feel free.

You can see our current site at http://www.tokelmo.gr

The colors should stay orange/black/grey.

In many of the "boxes/banners" we will need images. Feel free to find in glade barn as we have an account.

We have made notes throughout the wireframe that we have attached on what we are looking for. Let us know if you have any questions. Thanks.

Target Market(s)

People using technology and breaking it

Industry/Entity Type

It Service

Number of Pages Required

1 page

Font styles to use
Sans Serif

Requirements
Must have
• Must have a modern, professional look and feel. Need custom graphics and icons.

```html
<!DOCTYPE html>
<html lang="en">
<head>
<meta charset="utf-8">
<title>Tokelmo – Device Repairs</title>
<link href="https://fonts.googleapis.com/css2?family=Roboto:wght@300;400;500;700&display=swap" rel="stylesheet">
<style>
:root{
  --orange:#f5821f;
  --orange-dark:#e0701a;
  --ink:#1b1b1d;
  --ink-soft:#242427;
  --grey:#f4f4f4;
  --grey-line:#e3e3e3;
  --text:#333;
  --muted:#888;
  --white:#fff;
}
*{margin:0;padding:0;box-sizing:border-box}
html,body{width:1200px;height:3629px;overflow:hidden}
body{font-family:'Roboto',sans-serif;color:var(--text);background:var(--white);position:relative}
.abs{position:absolute}
/* top bar */
.topbar{top:0;left:0;width:1200px;height:29px;background:var(--ink)}
.quick-links{left:87px;top:0;height:29px;padding:0 16px;background:#333;color:#fff;font-size:12px;line-height:29px}
.lang{left:774px;top:0;line-height:29px;font-size:11px;color:#ccc}
.lang b{color:var(--orange);font-weight:400}
.top-social{left:850px;top:8px;display:flex;gap:22px}
.top-social span{width:12px;height:12px;border-radius:50%;background:#bbb;display:block}
/* header */
.header{top:29px;left:0;width:1200px;height:87px;background:#fff}
.logo{left:87px;top:30px;display:flex;align-items:center;gap:8px;font-size:28px;font-weight:500;color:var(--ink)}
.logo i{width:30px;height:30px;background:var(--orange);border-radius:6px;display:block}
.nav{left:618px;top:40px;display:flex;gap:30px;font-size:14px;color:#444}
.call{left:845px;top:26px;display:flex;gap:10px;align-items:center}
.call small,.support small{display:block;font-size:11px;color:var(--muted)}
.call strong,.support strong{font-size:14px;font-weight:500;color:var(--ink)}
.support{left:1010px;top:26px;display:flex;gap:10px;align-items:center}
/* hero */
.hero{top:116px;left:0;width:1200px;height:351px;background:linear-gradient(180deg,#3a2a26 0%,#5a4440 45%,#7a6c66 100%)}
.play{left:560px;top:256px;width:78px;height:78px;border-radius:50%;background:#fff;display:flex;align-items:center;justify-content:center}
/* counter */
.counter{top:467px;left:0;width:1200px;height:109px;background:var(--grey)}
.digits{left:162px;top:30px;display:flex;gap:10px}
.digits span{width:46px;height:50px;border:1px solid #ddd;background:#fff;color:var(--orange);font-size:24px;display:flex;align-items:center;justify-content:center}
.counter-text{left:462px;top:42px;font-size:17px;font-weight:500;color:#333}
/* feature grid */
.card{background:#555;color:#fff;overflow:hidden}
.card .cap{position:absolute;left:16px;bottom:14px;right:14px}
.card h3{font-size:16px;font-weight:700;text-transform:uppercase;margin-bottom:6px}
.card p{font-size:11.5px;line-height:1.45;color:#ddd}
.card a{font-size:11.5px;color:#fff}
/* repair section */
.repairs{top:1338px;left:0;width:1200px;height:421px;background:var(--orange);color:#fff}
.sec-title{width:100%;text-align:center;font-size:26px;font-weight:400}
.sec-title::after{content:"";display:block;width:44px;height:2px;background:currentColor;margin:8px auto 0;opacity:.8}
.repair-grid{left:87px;top:92px;width:1026px;display:grid;grid-template-columns:repeat(5,1fr)}
.repair-item{height:150px;display:flex;flex-direction:column;align-items:center;justify-content:center;gap:14px;font-size:13px;border-right:1px solid rgba(255,255,255,.2);border-bottom:1px solid rgba(255,255,255,.2)}
.repair-item:nth-child(5n){border-right:0}
.repair-item:nth-child(n+6){border-bottom:0}
/* options */
.options-title{top:1808px;left:0;color:#222}
.options{left:250px;top:1880px;width:700px;display:flex;justify-content:space-around}
.option{width:200px;text-align:center;font-size:14px;color:#444}
.option .ring{width:86px;height:86px;margin:0 auto 14px;border-radius:50%;border:1px solid var(--grey-line);display:flex;align-items:center;justify-content:center}
/* carousel */
.carousel{top:2050px;left:87px;width:1113px;height:338px;display:flex;gap:5px;overflow:hidden}
.carousel .card{position:relative;flex:0 0 251px;height:338px}
.arrow{width:24px;height:34px;background:rgba(255,255,255,.85);display:flex;align-items:center;justify-content:center}
/* testimonials */
.reviews-title{top:2434px;left:0;color:#222}
.stars{display:flex;gap:3px;justify-content:center}
.review{top:2541px;width:486px;height:266px;background:#fff;box-shadow:0 2px 14px rgba(0,0,0,.12);text-align:center;padding:34px 58px 0}
.review h4{color:var(--orange);font-size:14px;font-weight:400}
.review h5{font-size:12px;font-weight:400;color:#666;margin:4px 0 18px}
.review p{font-size:11.5px;line-height:1.7;color:#666;margin:14px 0}
.review cite{font-style:normal;font-size:17px;color:#444}
.dots{top:2856px;left:566px;display:flex;gap:12px}
.dots span{width:12px;height:12px;border-radius:50%;border:1px solid #bbb}
.dots .on{border-color:var(--orange);background:radial-gradient(var(--orange) 35%,transparent 40%)}
.tell{top:2887px;left:479px;width:242px;height:44px;background:#eee;font-size:13px;color:#444;display:flex;align-items:center;justify-content:center}
.chat-tab{top:2960px;left:852px;width:256px;height:42px;background:var(--orange);color:#fff;font-size:13px;display:flex;align-items:center;padding:0 14px;gap:14px}
/* footer */
.footer{top:3003px;left:0;width:1200px;height:626px;background:var(--ink);color:#fff}
.news-title{top:58px;font-size:24px;width:100%;text-align:center}
.news-sub{top:100px;font-size:12px;width:100%;text-align:center;color:#ccc}
.email{left:350px;top:138px;width:380px;height:42px;background:#2e2e31;color:#ddd;font-size:13px;padding:0 14px;line-height:42px}
.subscribe{left:738px;top:138px;width:108px;height:42px;background:#fff;color:#222;font-size:13px;text-align:center;line-height:42px}
.col h4{font-size:15px;font-weight:500;margin-bottom:14px}
.links li{list-style:none;font-size:12px;line-height:26px;color:#ddd}
.post{display:flex;gap:12px;margin-bottom:24px;font-size:12px;color:#ddd}
.post small{display:block;color:#999;font-size:11px;margin-top:3px}
.help h5{font-size:15px;font-weight:400;display:flex;align-items:center;gap:8px}
.help p{font-size:12px;color:#ddd;margin:6px 0 2px 28px}
.help em{font-style:normal;font-size:12px;color:var(--orange);margin-left:28px;display:block;margin-bottom:20px}
.foot-social{display:flex;gap:10px;margin-top:18px}
.foot-social span{width:26px;height:26px;border-radius:50%;background:#3a5ba0;display:block}
.rule{top:583px;left:87px;width:1026px;height:1px;background:#333}
.copy{top:596px;left:87px;font-size:11px;color:#ccc}
.cards-pay{top:590px;left:905px;display:flex;gap:6px}
.cards-pay span{width:46px;height:28px;border-radius:3px;background:#eee;display:block}
</style>
</head>
<body>

<div class="abs topbar">
  <div class="abs quick-links">Quick Links &#9662;</div>
  <div class="abs lang">GRE | <b>ENG</b></div>
  <div class="abs top-social"><span></span><span></span><span></span><span></span><span></span><span></span><span></span><span></span><span></span><span></span></div>
</div>

<header class="abs header">
  <div class="abs logo"><i></i>Tokelmo</div>
  <nav class="abs nav"><span>Repairs &#9662;</span><span>2 Stores &#9662;</span><span>Blog</span></nav>
  <div class="abs call">
    <svg width="22" height="34" viewBox="0 0 22 34"><rect x="2" y="1" width="18" height="32" rx="3" fill="none" stroke="#f5821f" stroke-width="2.5"/><circle cx="11" cy="28" r="1.6" fill="#f5821f"/></svg>
    <div><small>Call Us</small><strong>210 555 0142</strong></div>
  </div>
  <div class="abs support">
    <svg width="32" height="28" viewBox="0 0 32 28"><path d="M3 3h26v17H12l-7 6v-6H3z" fill="none" stroke="#f5821f" stroke-width="2.2" stroke-linejoin="round"/><circle cx="10" cy="11.5" r="1.6" fill="#f5821f"/><circle cx="16" cy="11.5" r="1.6" fill="#f5821f"/><circle cx="22" cy="11.5" r="1.6" fill="#f5821f"/></svg>
    <div><small>Support</small><strong>Live Chat</strong></div>
  </div>
</header>

<section class="abs hero" role="img" aria-label="Storefront of a Tokelmo repair shop with illuminated shop sign">
  <div class="abs play"><svg width="26" height="28" viewBox="0 0 26 28"><path d="M4 2l20 12L4 26z" fill="#f5821f"/></svg></div>
</section>

<section class="abs counter">
  <div class="abs digits"><span>0</span><span>1</span><span>2</span><span>3</span><span>4</span></div>
  <p class="abs counter-text">Repairs Completed With happy Customers. Yep, We Fix a Lot Of Devices!</p>
</section>

<div class="abs card" style="top:641px;left:87px;width:508px;height:292px;background:linear-gradient(135deg,#c9b8a4,#7d8a9a)" role="img" aria-label="Young couple looking at a map on a phone">
  <div class="cap"><h3>20 Tokelmo Locations</h3><p>Find a store Near You</p><a>View Map &raquo;</a></div>
</div>
<div class="abs card" style="top:641px;left:601px;width:508px;height:292px;background:linear-gradient(135deg,#e8e2dc,#8f7f74)" role="img" aria-label="Smiling woman holding up a smartphone">
  <div class="cap"><h3>Low Price Guarantee</h3><p>Find a lower Price For Your Phone Or Tabla Repair? We Will Match it *<br>* Terms and conditions apply, click to <a>Read More &raquo;</a></p></div>
</div>
<div class="abs card" style="top:939px;left:87px;width:251px;height:339px;background:linear-gradient(180deg,#6a6560,#2c2a28)" role="img" aria-label="Open service area inside the store">
  <div class="cap"><h3>Open Service Area</h3><p>Repairs right in front of you no closed doors, no back rooms</p><a>Read More &raquo;</a></div>
</div>
<div class="abs card" style="top:939px;left:344px;width:251px;height:339px;background:linear-gradient(180deg,#7d7d80,#2a2a2c)" role="img" aria-label="Technician repairing a device at a workbench">
  <div class="cap"><h3>Save 50-75% on multiple repairs</h3><p>If You device needs more than 1 part replaced, save up to 75% on addition parts</p></div>
</div>
<div class="abs card" style="top:939px;left:601px;width:251px;height:339px;background:linear-gradient(180deg,#6d7d8c,#2b2f35)" role="img" aria-label="Wall of phone accessories on display">
  <div class="cap"><h3>Accessories</h3></div>
</div>
<div class="abs card" style="top:939px;left:858px;width:251px;height:339px;background:linear-gradient(180deg,#bdbdbf,#4a4a4d)" role="img" aria-label="Hand holding a phone with a cracked screen">
  <div class="cap"><h3>20 Minute Repairs</h3><p>Most repairs can be completed in about 20 minutes.</p></div>
</div>

<section class="abs repairs">
  <h2 class="abs sec-title" style="top:48px">What We Repair</h2>
  <div class="abs repair-grid">
    <div class="repair-item"><svg width="26" height="46" viewBox="0 0 26 46"><rect x="2" y="2" width="22" height="42" rx="4" fill="none" stroke="#fff" stroke-width="2.2"/><line x1="10" y1="39" x2="16" y2="39" stroke="#fff" stroke-width="2"/></svg>Fonio Repair</div>
    <div class="repair-item"><svg width="38" height="48" viewBox="0 0 38 48"><rect x="2" y="2" width="34" height="44" rx="4" fill="none" stroke="#fff" stroke-width="2.2"/><circle cx="19" cy="40" r="2" fill="#fff"/></svg>Tabla Repair</div>
    <div class="repair-item"><svg width="44" height="50" viewBox="0 0 44 50"><rect x="2" y="2" width="30" height="42" rx="3" fill="none" stroke="#fff" stroke-width="2.2"/><line x1="8" y1="14" x2="26" y2="14" stroke="#fff" stroke-width="2"/><line x1="8" y1="22" x2="26" y2="22" stroke="#fff" stroke-width="2"/><path d="M28 30l12 12-4 4-12-12z" fill="#fff"/></svg>Tabla Touch Repair</div>
    <div class="repair-item"><svg width="28" height="48" viewBox="0 0 28 48"><rect x="2" y="2" width="24" height="44" rx="4" fill="none" stroke="#fff" stroke-width="2.2"/><line x1="2" y1="8" x2="26" y2="8" stroke="#fff" stroke-width="2"/><line x1="2" y1="38" x2="26" y2="38" stroke="#fff" stroke-width="2"/></svg>Somang Repair</div>
    <div class="repair-item"><svg width="30" height="48" viewBox="0 0 30 48"><rect x="2" y="2" width="26" height="44" rx="4" fill="none" stroke="#fff" stroke-width="2.2"/><rect x="7" y="8" width="16" height="12" fill="none" stroke="#fff" stroke-width="1.6"/><g fill="#fff"><rect x="7" y="25" width="4" height="3"/><rect x="13" y="25" width="4" height="3"/><rect x="19" y="25" width="4" height="3"/><rect x="7" y="31" width="4" height="3"/><rect x="13" y="31" width="4" height="3"/><rect x="19" y="31" width="4" height="3"/></g></svg>Somang Repair</div>
    <div class="repair-item"><svg width="56" height="46" viewBox="0 0 56 46"><rect x="2" y="2" width="52" height="32" rx="2" fill="none" stroke="#fff" stroke-width="2.2"/><path d="M22 34l-3 9h18l-3-9" fill="none" stroke="#fff" stroke-width="2.2"/></svg>Deskio Repairs</div>
    <div class="repair-item"><svg width="60" height="40" viewBox="0 0 60 40"><rect x="8" y="2" width="44" height="30" rx="2" fill="none" stroke="#fff" stroke-width="2.2"/><path d="M2 34h56l-3 4H5z" fill="#fff"/></svg>Notio Repair</div>
    <div class="repair-item"><svg width="62" height="46" viewBox="0 0 62 46"><rect x="2" y="2" width="42" height="30" fill="none" stroke="#fff" stroke-width="2.2"/><line x1="23" y1="32" x2="23" y2="42" stroke="#fff" stroke-width="2.2"/><line x1="14" y1="43" x2="32" y2="43" stroke="#fff" stroke-width="2.2"/><rect x="48" y="2" width="12" height="42" fill="none" stroke="#fff" stroke-width="2.2"/></svg>Computer Repair</div>
    <div class="repair-item"><svg width="60" height="40" viewBox="0 0 60 40"><rect x="8" y="2" width="44" height="30" rx="2" fill="none" stroke="#fff" stroke-width="2.2"/><path d="M2 34h56v3H2z" fill="#fff"/></svg>Laptop Repair</div>
    <div class="repair-item"><svg width="44" height="50" viewBox="0 0 44 50"><path d="M22 10a12 12 0 0 0-7 22v6h14v-6a12 12 0 0 0-7-22z" fill="#fff"/><rect x="16" y="40" width="12" height="4" fill="#fff"/><g stroke="#fff" stroke-width="2"><line x1="22" y1="1" x2="22" y2="6"/><line x1="4" y1="22" x2="8" y2="22"/><line x1="36" y1="22" x2="40" y2="22"/><line x1="9" y1="9" x2="12" y2="12"/><line x1="35" y1="9" x2="32" y2="12"/></g></svg>Business Services</div>
  </div>
</section>

<h2 class="abs sec-title options-title">Repair Options</h2>
<div class="abs options">
  <div class="option"><div class="ring"><svg width="40" height="28" viewBox="0 0 40 28"><path d="M2 4h22v16H2zM24 10h8l6 6v4H24z" fill="#f5821f"/><circle cx="10" cy="22" r="4" fill="#f5821f" stroke="#fff" stroke-width="2"/><circle cx="31" cy="22" r="4" fill="#f5821f" stroke="#fff" stroke-width="2"/></svg></div>Find a Store Near You ?</div>
  <div class="option"><div class="ring"><svg width="30" height="36" viewBox="0 0 30 36"><path d="M3 8h24v26H3z" fill="none" stroke="#f5821f" stroke-width="2.4"/><path d="M10 8V4h10v4" fill="none" stroke="#f5821f" stroke-width="2.4"/><rect x="11" y="14" width="8" height="10" fill="#f5821f"/></svg></div>Send Us Your Device ?</div>
  <div class="option"><div class="ring"><svg width="32" height="38" viewBox="0 0 32 38"><path d="M16 36S3 22 3 14a13 13 0 0 1 26 0c0 8-13 22-13 22z" fill="none" stroke="#f5821f" stroke-width="2.4"/><text x="16" y="20" text-anchor="middle" font-family="Roboto,sans-serif" font-size="14" font-weight="700" fill="#f5821f">$</text></svg></div>Free Pickup in Athens</div>
</div>

<div class="abs carousel">
  <div class="card" style="background:linear-gradient(180deg,#5f5f62,#232325)" role="img" aria-label="Technicians at the open service counter"><div class="cap"><h3>Open Service Area</h3></div></div>
  <div class="card" style="background:linear-gradient(180deg,#4a4c52,#1e1f22)" role="img" aria-label="Staff serving customers at the repair bar"><div class="cap"><h3>Save 50-75% on multiple repairs</h3></div></div>
  <div class="card" style="background:linear-gradient(180deg,#7a6e64,#2a2522)" role="img" aria-label="Store interior with accessory displays"><div class="cap"><h3>Accessories</h3></div></div>
  <div class="card" style="background:linear-gradient(180deg,#6a8298,#2a323c)" role="img" aria-label="Shop front with illuminated sign"><div class="cap"><h3>20 Minute Repairs</h3></div></div>
  <div class="card" style="background:linear-gradient(180deg,#8a8a8c,#3a3a3c)" role="img" aria-label="Accessories display"><div class="cap"><h3>Accessories</h3></div></div>
</div>
<div class="abs arrow" style="top:2202px;left:87px"><svg width="8" height="12" viewBox="0 0 8 12"><path d="M7 1L2 6l5 5" fill="none" stroke="#333" stroke-width="2"/></svg></div>
<div class="abs arrow" style="top:2202px;left:1128px"><svg width="8" height="12" viewBox="0 0 8 12"><path d="M1 1l5 5-5 5" fill="none" stroke="#333" stroke-width="2"/></svg></div>

<h2 class="abs sec-title reviews-title">What Our Customers say</h2>
<div class="abs stars" style="top:2494px;left:0;width:1200px">
  <svg width="84" height="16" viewBox="0 0 84 16"><g fill="#f5a623"><path id="st" d="M8 0l2.4 5 5.6.7-4 3.9 1 5.5L8 12.5 3 15.1l1-5.5-4-3.9L5.6 5z"/><use href="#st" x="17"/><use href="#st" x="34"/><use href="#st" x="51"/></g><path d="M76 0l2.4 5 5.6.7-4 3.9 1 5.5L76 12.5z" fill="#f5a623"/></svg>
</div>

<div class="abs review" style="left:-420px;opacity:.9"></div>
<article class="abs review" style="left:106px">
  <h4>Laptop Repair</h4><h5>Overheating</h5>
  <div class="stars"><svg width="84" height="14" viewBox="0 0 84 16"><g fill="#f5a623"><use href="#st"/><use href="#st" x="17"/><use href="#st" x="34"/><use href="#st" x="51"/></g><path d="M76 0l2.4 5 5.6.7-4 3.9 1 5.5L76 12.5z" fill="#f5a623"/></svg></div>
  <p>There are many variations of passages of Lorem Ipsum available, but the majority have suffered alteration in some form, by injected humour, or randomised words which don't look even slightly believable.</p>
  <cite>Eleni P., Chalandri</cite>
</article>
<article class="abs review" style="left:610px">
  <h4>Fonio 6 Repair</h4><h5>Screen Replacement</h5>
  <div class="stars"><svg width="84" height="14" viewBox="0 0 84 16"><g fill="#f5a623"><use href="#st"/><use href="#st" x="17"/><use href="#st" x="34"/><use href="#st" x="51"/></g><path d="M76 0l2.4 5 5.6.7-4 3.9 1 5.5L76 12.5z" fill="#f5a623"/></svg></div>
  <p>There are many variations of passages of Lorem Ipsum available, but the majority have suffered alteration in some form, by injected humour, or randomised words which don't look even slightly believable.</p>
  <cite>Marina T., Peristeri</cite>
</article>
<div class="abs review" style="left:1140px;opacity:.9"></div>

<div class="abs dots"><span></span><span class="on"></span><span></span></div>
<div class="abs tell">Tell us about Tokelmo experience</div>

<div class="abs chat-tab">
  <svg width="20" height="18" viewBox="0 0 20 18"><path d="M2 2h16v10H8l-4 4v-4H2z" fill="none" stroke="#fff" stroke-width="1.8"/></svg>
  <span style="flex:1">Tokelmo Live Chat</span>
  <svg width="12" height="8" viewBox="0 0 12 8"><path d="M1 7l5-5 5 5" fill="none" stroke="#fff" stroke-width="2"/></svg>
</div>

<footer class="abs footer">
  <h2 class="abs news-title" style="font-weight:400">Newsletter</h2>
  <p class="abs news-sub">* Subscribe to the Tokelmo newsletter</p>
  <div class="abs email">Email address</div>
  <div class="abs subscribe">Subscribe</div>

  <div class="abs col" style="left:87px;top:258px">
    <h4>Quick Links</h4>
    <ul class="links"><li>About Tokelmo</li><li>Business Services</li><li>Schedule a Pickup</li><li>Job openings</li><li>Shipping Instructions</li><li>Privacy policy</li><li>Send your device with ParcelNest</li></ul>
    <div class="foot-social"><span></span><span style="background:#2aa3ef"></span><span style="background:#d9483b"></span><span style="background:#1b7bb8"></span><span style="background:#c8232c"></span><span style="background:#3f729b"></span><span style="background:#e52d27"></span></div>
  </div>

  <div class="abs col" style="left:480px;top:258px;width:300px">
    <h4>Tokelmo Blog</h4>
    <div class="post"><span>&#9656;</span><div>Tokelmo Corfu Seminar<small>20/03/2017</small></div></div>
    <div class="post"><span>&#9656;</span><div>Orchard announces DevMeet 2017<small>17/02/2017</small></div></div>
    <div class="post"><span>&#9656;</span><div>They use Nuttina as thermal paste [video]<small>05/02/2017</small></div></div>
  </div>

  <div class="abs col help" style="left:866px;top:258px;width:260px">
    <h4>Can't find what you need?</h4>
    <h5><svg width="18" height="14" viewBox="0 0 18 14"><rect x="1" y="1" width="16" height="12" fill="none" stroke="#fff" stroke-width="1.6"/><path d="M1 1l8 7 8-7" fill="none" stroke="#fff" stroke-width="1.6"/></svg>Email Support</h5>
    <p>We usually respond within 24 hours</p><em>Click to send email</em>
    <h5 style="margin-left:0">Contact our call center</h5>
    <p>Call to speak to a customer service rep.</p><em>210 555 0142</em>
    <h5><svg width="18" height="16" viewBox="0 0 18 16"><path d="M1 1h16v10H7l-4 4v-4H1z" fill="none" stroke="#fff" stroke-width="1.6"/></svg>Live Chat</h5>
    <p>Chat with an Tokelmo technician now.</p><em>Click to chat</em>
  </div>

  <div class="abs rule"></div>
  <p class="abs copy">&copy; Tokelmo 2017</p>
  <div class="abs cards-pay"><span></span><span></span><span></span><span></span></div>
</footer>

</body>
</html>
```